Need Business Card for our Indian Grocery Store

Industry/Entity Type

Grocery Store

Contact Information for Business Card

Manoj Baweja
Director

Store Locations:

Ashborough
482 Elm Parade
P: 03 9172 5843

Glenmerit
613 Carlow Road
P: 03 9238 6014

email: kvtmarts@mailnest.example

Requirements
Must have
• Our logo Colours

```html
<!DOCTYPE html>
<html lang="en">
<head>
<meta charset="utf-8">
<title>KVT Marts – Business Card</title>
<link href="https://fonts.googleapis.com/css2?family=Lato:wght@400;700&display=swap" rel="stylesheet">
<style>
  :root {
    --card-red: #e20f05;
    --card-white: #ffffff;
    --circle-light: #fbfbfb;
    --circle-shade: #dcdcdc;
    --page-bg: #eceae8;
  }
  * { margin: 0; padding: 0; box-sizing: border-box; }
  html, body {
    width: 1200px;
    height: 900px;
    overflow: hidden;
    background: var(--page-bg);
    font-family: "Lato", sans-serif;
  }
  .business-card {
    position: absolute;
    left: 210px;
    top: 210px;
    width: 780px;
    height: 480px;
    background: var(--card-red);
    border-radius: 22px;
    color: var(--card-white);
    overflow: hidden;
  }
  .contact-name {
    position: absolute;
    left: 40px;
    top: 52px;
    font-weight: 700;
    font-size: 25px;
    letter-spacing: 0.5px;
    text-transform: uppercase;
    line-height: 1.1;
  }
  .contact-role {
    position: absolute;
    left: 40px;
    top: 80px;
    font-size: 21px;
    line-height: 1.2;
  }
  .store {
    position: absolute;
    left: 43px;
    font-size: 21px;
    line-height: 29px;
  }
  .store--north { top: 181px; }
  .store--south { top: 280px; }
  .store-suburb { text-transform: uppercase; letter-spacing: 0.3px; }
  .contact-email {
    position: absolute;
    left: 43px;
    top: 392px;
    font-size: 21px;
    display: flex;
    align-items: center;
    gap: 6px;
  }
  .contact-email svg { width: 15px; height: 11px; }
  .brand-disc {
    position: absolute;
    left: 339px;
    top: 31px;
    width: 416px;
    height: 416px;
    border-radius: 50%;
    background: radial-gradient(circle at 45% 40%, var(--circle-light) 0%, #f2f2f2 55%, var(--circle-shade) 100%);
    display: flex;
    align-items: center;
    justify-content: center;
  }
  .brand-name {
    color: var(--card-red);
    font-weight: 700;
    font-size: 60px;
    letter-spacing: 1px;
  }
</style>
</head>
<body>
  <div class="business-card">
    <div class="contact-name">Manoj Baweja</div>
    <div class="contact-role">Director</div>

    <div class="store store--north">
      <div class="store-suburb">Ashborough</div>
      <div class="store-address">482 Elm Parade</div>
      <div class="store-phone">P: 03 9172 5843</div>
    </div>

    <div class="store store--south">
      <div class="store-suburb">Glenmerit</div>
      <div class="store-address">613 Carlow Road</div>
      <div class="store-phone">P: 03 9238 6014</div>
    </div>

    <div class="contact-email">
      <svg viewBox="0 0 15 11" aria-hidden="true">
        <rect x="0" y="0" width="15" height="11" fill="#ffffff"/>
        <path d="M0.5 0.8 L7.5 6 L14.5 0.8" fill="none" stroke="#e20f05" stroke-width="1.3"/>
      </svg>
      <span>kvtmarts@mailnest.example</span>
    </div>

    <div class="brand-disc">
      <span class="brand-name">KVT Marts</span>
    </div>
  </div>
</body>
</html>
```